Global (re)insurance broker needs a business card design

We need a classic business card for our company that is headquartered in SG, with offices in Malaysia and Dubai. We specialise in insurance and reinsurance broking and consultancy for our global clients.

```html
<!DOCTYPE html>
<html lang="en">
<head>
<meta charset="utf-8">
<title>Veranor Business Card</title>
<link rel="stylesheet" href="https://fonts.googleapis.com/css2?family=Open+Sans:wght@400;600;700;800&display=swap">
<style>
  :root {
    --stage: #222222;
    --brand-blue: #24479c;
    --brand-blue-deep: #1f3f8f;
    --brand-blue-soft: #3557ad;
    --brand-green: #c3dfba;
    --ink: #1c1c1c;
    --paper: #ffffff;
    --rule: #2a2a2a;
  }
  * { box-sizing: border-box; margin: 0; padding: 0; }
  html, body {
    width: 1200px; height: 780px; overflow: hidden;
    background: var(--stage);
    font-family: "Open Sans", Arial, sans-serif;
  }
  .canvas {
    position: relative; width: 1200px; height: 780px;
    display: flex; align-items: center; justify-content: center; gap: 40px;
  }
  .card {
    position: relative; width: 540px; height: 309px;
    border-radius: 18px; overflow: hidden;
  }

  /* Back of card */
  .card--back { background: var(--brand-blue); }
  .card--back .pattern-area {
    position: absolute; inset: 0;
    background: linear-gradient(160deg, var(--brand-blue-soft) 0%, var(--brand-blue) 45%, var(--brand-blue-deep) 100%);
  }
  .card--back .wordmark {
    position: absolute; left: 0; right: 0; top: 50%;
    transform: translateY(-50%);
    text-align: center;
    color: var(--paper);
    font-weight: 800; font-size: 62px; letter-spacing: 2px;
  }

  /* Front of card */
  .card--front { background: var(--paper); }
  .card--front .wordmark {
    position: absolute; left: 34px; top: 128px;
    color: var(--brand-blue);
    font-weight: 800; font-size: 44px; letter-spacing: 1px;
  }
  .divider {
    position: absolute; left: 262px; top: 50px;
    width: 1px; height: 150px; background: var(--rule);
  }
  .contact-block { position: absolute; left: 290px; top: 44px; }
  .person-name {
    font-weight: 800; font-size: 32px; line-height: 1;
    color: var(--brand-blue);
  }
  .person-name .surname { color: var(--brand-green); }
  .person-title {
    margin-top: 4px; font-weight: 600; font-size: 14px; color: var(--ink);
  }
  .contact-list { list-style: none; margin-top: 18px; }
  .contact-list li {
    display: flex; align-items: center; gap: 8px;
    font-size: 13px; line-height: 22px; color: var(--ink);
  }
  .contact-list svg { width: 14px; height: 14px; flex: none; }
  .address {
    position: absolute; left: 34px; top: 238px;
    font-size: 12.5px; color: var(--ink);
  }
  .bottom-bands { position: absolute; left: 0; bottom: 0; width: 540px; height: 60px; }
</style>
</head>
<body>
<main class="canvas">
  <section class="card card--back" aria-label="Card back">
    <div class="pattern-area" role="img" aria-label="Repeated company wordmark pattern in blue tones"></div>
    <div class="wordmark">VERANOR</div>
  </section>

  <section class="card card--front" aria-label="Card front">
    <div class="wordmark">VERANOR</div>
    <div class="divider"></div>
    <div class="contact-block">
      <h1 class="person-name">Mira <span class="surname">Lim</span></h1>
      <p class="person-title">Chief Operating Officer</p>
      <ul class="contact-list">
        <li>
          <svg viewBox="0 0 14 14" aria-hidden="true"><rect x="3.5" y="1" width="7" height="12" rx="1.2" fill="none" stroke="#c3dfba" stroke-width="1.3"/></svg>
          +65 9123 4567
        </li>
        <li>
          <svg viewBox="0 0 14 14" aria-hidden="true"><circle cx="7" cy="7" r="6" fill="#24479c"/><path d="M1 7h12M7 1c-2.5 3-2.5 9 0 12M7 1c2.5 3 2.5 9 0 12" stroke="#fff" stroke-width="0.9" fill="none"/></svg>
          www.veranor.com
        </li>
        <li>
          <svg viewBox="0 0 14 14" aria-hidden="true"><rect x="1" y="3" width="12" height="8.5" rx="1" fill="#c3dfba"/><path d="M1.5 3.5 7 8l5.5-4.5" stroke="#fff" stroke-width="1.1" fill="none"/></svg>
          mira@veranor.com
        </li>
      </ul>
    </div>
    <p class="address">25 Harbour Lane, Marina Tower #08-04, Singapore 049315</p>
    <svg class="bottom-bands" viewBox="0 0 540 60" aria-hidden="true">
      <polygon points="330,42 540,14 540,60 345,60" fill="#c3dfba"/>
      <polygon points="0,42 322,42 345,60 0,60" fill="#24479c"/>
    </svg>
  </section>
</main>
</body>
</html>
```